Property inspection company needs logo/business card design

A new, home, commercial, and multi dwelling inspection company needs help with a new logo and hence business cards.

Time is extended for the rest of the week.

Font styles to use
Sans Serif

Colors
ec1f27
0255a3
ffffff

```html
<!DOCTYPE html>
<html lang="en">
<head>
<meta charset="utf-8">
<title>Noel Harwick Property Inspections – Business Card</title>
<link rel="stylesheet" href="https://fonts.googleapis.com/css2?family=Montserrat:wght@600;700&family=Quicksand:wght@400;500&display=swap">
<style>
  :root {
    --brand-red: #ec1f27;
    --brand-blue: #0255a3;
    --card-white: #ffffff;
    --ink-grey: #5a5f66;
    --backdrop: #e4e5e7;
  }
  * { margin: 0; padding: 0; box-sizing: border-box; }
  html, body {
    width: 1200px;
    height: 915px;
    overflow: hidden;
    background: var(--backdrop);
  }
  .stage {
    width: 1200px;
    height: 915px;
    display: flex;
    align-items: center;
    justify-content: center;
  }
  .business-card {
    position: relative;
    width: 840px;
    height: 580px;
    background: var(--card-white);
    box-shadow: 0 6px 18px rgba(0, 0, 0, 0.12);
  }
  .brand-name {
    position: absolute;
    left: 64px;
    top: 62px;
    font-family: "Montserrat", sans-serif;
    font-weight: 700;
    color: var(--brand-blue);
    line-height: 1.15;
  }
  .brand-name .brand-primary {
    display: block;
    font-size: 40px;
    letter-spacing: 1px;
  }
  .brand-name .brand-secondary {
    display: block;
    margin-top: 6px;
    font-size: 15px;
    letter-spacing: 5.2px;
  }
  .holder {
    position: absolute;
    left: 64px;
    top: 398px;
    display: flex;
    align-items: baseline;
    gap: 10px;
  }
  .holder-name {
    font-family: "Montserrat", sans-serif;
    font-weight: 600;
    font-size: 21px;
    letter-spacing: 2.4px;
    color: var(--brand-blue);
  }
  .holder-divider {
    font-family: "Montserrat", sans-serif;
    font-weight: 600;
    font-size: 22px;
    color: var(--brand-blue);
  }
  .holder-role {
    font-family: "Quicksand", sans-serif;
    font-weight: 500;
    font-size: 21px;
    color: var(--ink-grey);
  }
  .accent-rule {
    position: absolute;
    left: 56px;
    right: 36px;
    top: 440px;
    height: 3px;
    background: var(--brand-red);
  }
  .contact-item {
    position: absolute;
    display: flex;
    align-items: center;
    gap: 14px;
    font-family: "Quicksand", sans-serif;
    font-weight: 500;
    font-size: 22px;
    letter-spacing: 0.4px;
    color: var(--ink-grey);
  }
  .contact-item svg { flex: none; }
  .contact-email { left: 60px; top: 458px; }
  .contact-phone { right: 40px; top: 398px; }
  .contact-web { right: 40px; top: 462px; }
</style>
</head>
<body>
<main class="stage">
  <article class="business-card">
    <h1 class="brand-name">
      <span class="brand-primary">NOEL HARWICK</span>
      <span class="brand-secondary">PROPERTY INSPECTIONS INC.</span>
    </h1>

    <div class="holder">
      <span class="holder-name">DARIN KOVALEV</span>
      <span class="holder-divider">|</span>
      <span class="holder-role">Manager</span>
    </div>

    <div class="accent-rule"></div>

    <p class="contact-item contact-email">
      <svg width="18" height="14" viewBox="0 0 18 14" aria-hidden="true">
        <rect x="1" y="1" width="16" height="12" rx="1.5" fill="none" stroke="var(--brand-blue)" stroke-width="1.8"/>
        <path d="M1.5 2 L9 8 L16.5 2" fill="none" stroke="var(--brand-blue)" stroke-width="1.8"/>
      </svg>
      info@noelharwick.com
    </p>

    <p class="contact-item contact-phone">
      <svg width="14" height="18" viewBox="0 0 14 18" aria-hidden="true">
        <path d="M3 1 L6 1 L7 5 L5 6.5 C5.8 9 7 11 9 12.5 L10.8 11 L13.5 12.5 L13 16 C12.5 17 11 17.3 9.5 16.5 C5 14 1.5 9 1 4 C1 2.5 1.8 1.2 3 1 Z" fill="var(--brand-blue)"/>
      </svg>
      555-014-2290
    </p>

    <p class="contact-item contact-web">
      <svg width="18" height="18" viewBox="0 0 18 18" aria-hidden="true">
        <circle cx="9" cy="9" r="7.6" fill="none" stroke="var(--brand-blue)" stroke-width="1.6"/>
        <ellipse cx="9" cy="9" rx="3.4" ry="7.6" fill="none" stroke="var(--brand-blue)" stroke-width="1.4"/>
        <path d="M1.6 9 H16.4 M3 5 H15 M3 13 H15" stroke="var(--brand-blue)" stroke-width="1.3"/>
      </svg>
      www.noelharwick.com
    </p>
  </article>
</main>
</body>
</html>
```